red mesa (las vegas) mobile detailing needs a logo design

I am in need of a logo and design for my mobile detailing business based out of Las Vegas NV. The service provides detailing for all types of transportation. Auto, boat, RV, aircraft, motorcycle.
standard wash and dry to a full detail with hand wax. We come to your home or place of business
I have a haulbrook van that i would also like to use the design on.
Be sure to utilize the city of las vegas as well as the desert it exists in.

```html
<!DOCTYPE html>
<html lang="en">
<head>
<meta charset="utf-8">
<title>red mesa Mobile Detailing</title>
<link rel="stylesheet" href="https://fonts.googleapis.com/css2?family=Arimo:wght@400;700&display=swap">
<style>
  :root {
    --brand-blue: #1560f2;
    --ink: #111111;
    --paper: #ffffff;
  }
  html, body {
    margin: 0;
    padding: 0;
    overflow: hidden;
    background: var(--paper);
  }
  .card {
    position: relative;
    width: 1200px;
    height: 668px;
    background: var(--paper);
    overflow: hidden;
    font-family: "Arimo", Arial, sans-serif;
  }
  .brand-square {
    position: absolute;
    left: 80px;
    top: 108px;
    width: 120px;
    height: 120px;
    background: var(--brand-blue);
  }
  .brand-name {
    position: absolute;
    left: 388px;
    top: 112px;
    margin: 0;
    font-size: 128px;
    font-weight: 700;
    line-height: 1;
    letter-spacing: 2px;
    color: var(--brand-blue);
  }
  .tagline {
    position: absolute;
    left: 0;
    width: 1352px;
    top: 250px;
    margin: 0;
    text-align: center;
    font-size: 36px;
    font-weight: 400;
    color: var(--ink);
  }
  .services {
    position: absolute;
    left: 0;
    width: 1200px;
    top: 368px;
    margin: 0;
    text-align: center;
    font-size: 38px;
    color: var(--ink);
  }
  .wave {
    position: absolute;
    left: 0;
    top: 0;
  }
  .call-to-action {
    position: absolute;
    left: 0;
    width: 1200px;
    top: 524px;
    margin: 0;
    text-align: center;
    font-size: 41px;
    color: var(--paper);
  }
  .phone {
    position: absolute;
    left: 0;
    width: 1200px;
    top: 580px;
    margin: 0;
    text-align: center;
    font-size: 45px;
    font-weight: 700;
    color: var(--paper);
  }
</style>
</head>
<body>
<main class="card">
  <div class="brand-square"></div>
  <h1 class="brand-name">red mesa</h1>
  <p class="tagline">Mobile Detailing</p>
  <p class="services">Auto, Boat, Motorcycle, Aircraft, rv</p>

  <svg class="wave" width="1200" height="668" viewBox="0 0 1200 668" aria-hidden="true">
    <path d="M0 426 C 180 470, 380 500, 620 470 C 820 445, 1000 420, 1200 432"
          fill="none" stroke="var(--brand-blue)" stroke-width="7"/>
    <path d="M0 446 C 180 490, 380 520, 620 488 C 820 462, 1000 440, 1200 452 L1200 668 L0 668 Z"
          fill="var(--brand-blue)"/>
  </svg>

  <p class="call-to-action">call now to schedule your detail</p>
  <p class="phone">(702) 555-0148</p>
</main>
</body>
</html>
```